Property Management Card

We are owners of a property management and real estate company. We manage many residential buildings in our area and would like to send cards to neighboring propertiies. I have attached a card that was designed for us that we do not like but has pertinent information and branding, font style, etc. We want something that will grab people's attention as they sift through their junk mail.

Here is information we would like included:

We manage the property at________(we will fill in the blank)
We can manage yours, too!

We offer
24 hour emergency line
online rent payment for tenants
the best trades people in the South Bay
5 full time employees who speak English and Spanish
Business for over 36 years

Call Mark Holloway for a free quote at 310-847-2093

Target Market(s)

Industry/Entity Type

Real Estate

Requirements
Must have
• We manage the property at________(we will fill in the blank)
• We can manage yours, too!
• We offer
• 24 hour emergency line
• online rent payment for tenants
• the best trades people in the South Bay
• 5 full time employees who speak English and Spanish
• Business for over 36 years
• Call Mark Holloway for a free quote at 310-847-2093
• Email address mark@brindlecrestmgmt.com
• website brindlecrestharborproperties.com
• Broker BRE 04817352
• office address is
• 18 Tessaly Court, Suite 4
• Palos Verdes Estates, CA 90318
• two sided
• space for a mailing address and postage
• our branding/logo
• font to coordinate with branding
• postcard to be 279mm x 152 mm (full bleed size is 282 mm x 155mm, 3335x1835 pixels)
• vertical or horizontal orientation up to designers creativity. Again, what ever will draw attention
• (our branding colors are a dark gray/charcoal, white and dark sand. see postcard and logo for example of colors)
Nice to have
• images to draw attention to owners who would like a property manager
• we would like to have our photo. if this compromises design then we are happy to delete it. the photo can be on either side

```html
<!DOCTYPE html>
<html lang="en">
<head>
<meta charset="utf-8">
<title>Brindlecrest Harbor – Property Management Postcard</title>
<link rel="stylesheet" href="https://fonts.googleapis.com/css2?family=Open+Sans:wght@400;600;700&display=swap">
<style>
  :root {
    --backdrop: #968f7f;
    --charcoal: #3a3633;
    --sand: #948e7e;
    --sand-light: #a9a290;
    --white: #ffffff;
    --paper: #f7f6f3;
    --line: #5a5652;
  }
  * { margin: 0; padding: 0; box-sizing: border-box; }
  html, body { width: 1200px; height: 811px; overflow: hidden; }
  body {
    background: var(--backdrop);
    font-family: "Open Sans", Arial, sans-serif;
    color: var(--white);
    position: relative;
  }
  .card { position: absolute; width: 573px; height: 312px; overflow: hidden; }

  /* ---------- Front side ---------- */
  .front { left: 159px; top: 83px; background: var(--charcoal); }
  .front .center { position: absolute; left: 0; width: 100%; text-align: center; white-space: nowrap; }
  .front .headline { font-weight: 700; font-size: 12.5px; letter-spacing: .1px; }
  .front .title-top { top: 19px; }
  .front .fill-band { position: absolute; left: 0; top: 37px; width: 100%; height: 30px; background: var(--white); }
  .front .title-yours { top: 70px; font-size: 13px; }
  .front .offer { top: 95px; font-size: 9.6px; line-height: 12.2px; text-transform: uppercase; }
  .front .offer strong { font-weight: 700; }
  .front .cta {
    position: absolute; left: 50%; top: 180px; transform: translateX(-50%);
    height: 22px; padding: 0 12px; white-space: nowrap;
    border: 1px solid var(--white); font-size: 9.2px; line-height: 20px; text-align: center;
  }
  .front .broker { top: 206px; font-size: 11px; }
  .front .divider { position: absolute; left: 0; top: 230px; width: 100%; height: 4px; background: var(--sand); }
  .front .portrait {
    position: absolute; left: 23px; top: 208px; width: 60px; height: 79px;
    background: linear-gradient(135deg, #8c8a86, #3b3835 70%, #24211f);
  }
  .brand-name { font-weight: 400; color: var(--white); line-height: 1; }
  .brand-tagline { font-size: 4px; letter-spacing: 1.2px; color: var(--white); text-transform: uppercase; white-space: nowrap; }
  .front .brand { position: absolute; left: 92px; top: 249px; }
  .front .brand-name { font-size: 13px; }
  .front .brand-tagline { margin-top: 6px; }

  .contacts { position: absolute; font-size: 7.6px; line-height: 10.4px; list-style: none; white-space: nowrap; }
  .contacts li { display: flex; align-items: center; gap: 6px; }
  .contacts svg { width: 8px; height: 8px; flex: none; fill: var(--sand-light); }
  .contacts li.no-icon { padding-left: 14px; }
  .front .contacts { left: 409px; top: 251px; }

  /* ---------- Back side ---------- */
  .back { left: 468px; top: 415px; background: var(--paper); }
  .back .panel { position: absolute; inset: 0; width: 100%; height: 100%; }
  .back .brand { position: absolute; left: 27px; top: 24px; }
  .back .brand-name { font-size: 21px; }
  .back .brand-tagline { font-size: 5.6px; letter-spacing: 1.6px; margin-top: 10px; }
  .back .offer-bar {
    position: absolute; left: 0; top: 113px; height: 21px; white-space: nowrap;
    font-weight: 700; font-size: 9.2px; line-height: 21px; padding-left: 28px;
  }
  .back .benefits { position: absolute; left: 29px; top: 139px; list-style: none; font-size: 8.4px; line-height: 14.4px; white-space: nowrap; }
  .back .benefits li { display: flex; gap: 7px; }
  .back .benefits svg { width: 8px; height: 8px; margin-top: 3px; flex: none; }
  .back .benefits li.wrap { padding-left: 15px; }
  .back .contacts { left: 28px; top: 253px; }
  .back .stamp { position: absolute; left: 491px; top: 36px; width: 43px; height: 44px; border: 1px solid var(--line); }
  .back .address-line { position: absolute; left: 345px; width: 189px; height: 1px; background: var(--line); }
</style>
</head>
<body>

<!-- Front -->
<section class="card front">
  <p class="center headline title-top">WE MANAGE THE PROPERTY AT</p>
  <div class="fill-band"></div>
  <p class="center headline title-yours">WE CAN MANAGE YOURS</p>
  <p class="center offer">
    <strong>Here is what we have to offer</strong><br>
    24 hour emergency line<br>
    Online rent payment for tenants<br>
    The best trades people in the South Bay<br>
    5 full time employees who speak English and Spanish<br>
    Business for over 36 years
  </p>
  <p class="cta">Call Mark Holloway for a free quote at 310-847-2093</p>
  <p class="center broker">Broker BRE 04817352</p>
  <div class="divider"></div>
  <div class="portrait" role="img" aria-label="Photo of the broker team"></div>
  <div class="brand">
    <p class="brand-name">Brindlecrest<br>Harbor</p>
    <p class="brand-tagline">A boutique real estate agency</p>
  </div>
  <ul class="contacts">
    <li><svg viewBox="0 0 10 10"><path d="M0 2h10v6H0z M0 2l5 3.5L10 2" /></svg>mark@brindlecrestmgmt.com</li>
    <li><svg viewBox="0 0 10 10"><circle cx="5" cy="5" r="4.5"/></svg>brindlecrestharborproperties.com</li>
    <li><svg viewBox="0 0 10 10"><path d="M5 0a3.6 3.6 0 0 1 3.6 3.6C8.6 6.2 5 10 5 10S1.4 6.2 1.4 3.6A3.6 3.6 0 0 1 5 0z"/></svg>18 Tessaly Court, Suite 4</li>
    <li class="no-icon">Palos Verdes Estates, CA 90318</li>
  </ul>
</section>

<!-- Back -->
<section class="card back">
  <svg class="panel" viewBox="0 0 573 312" aria-hidden="true">
    <polygon points="0,0 344,0 240,312 0,312" fill="var(--charcoal)"/>
    <polygon points="0,113 304,113 297,134 0,134" fill="var(--sand)"/>
    <line x1="0" y1="244.5" x2="263" y2="244.5" stroke="var(--sand)" stroke-width="2"/>
  </svg>
  <div class="brand">
    <p class="brand-name">Brindlecrest<br>Harbor</p>
    <p class="brand-tagline">A boutique real estate agency</p>
  </div>
  <p class="offer-bar">HERE IS WHAT WE HAVE TO OFFER</p>
  <ul class="benefits">
    <li><svg viewBox="0 0 10 10"><circle cx="5" cy="5" r="4.3" fill="none" stroke="var(--sand-light)"/><path d="M3 5l1.6 1.6L8.5 2.8" fill="none" stroke="var(--sand-light)"/></svg>24 hour emergency line</li>
    <li><svg viewBox="0 0 10 10"><circle cx="5" cy="5" r="4.3" fill="none" stroke="var(--sand-light)"/><path d="M3 5l1.6 1.6L8.5 2.8" fill="none" stroke="var(--sand-light)"/></svg>Online rent payment for tenants</li>
    <li><svg viewBox="0 0 10 10"><circle cx="5" cy="5" r="4.3" fill="none" stroke="var(--sand-light)"/><path d="M3 5l1.6 1.6L8.5 2.8" fill="none" stroke="var(--sand-light)"/></svg>The best trades people in the South Bay</li>
    <li><svg viewBox="0 0 10 10"><circle cx="5" cy="5" r="4.3" fill="none" stroke="var(--sand-light)"/><path d="M3 5l1.6 1.6L8.5 2.8" fill="none" stroke="var(--sand-light)"/></svg>5 full time employees who speak</li>
    <li class="wrap">English and Spanish</li>
    <li><svg viewBox="0 0 10 10"><circle cx="5" cy="5" r="4.3" fill="none" stroke="var(--sand-light)"/><path d="M3 5l1.6 1.6L8.5 2.8" fill="none" stroke="var(--sand-light)"/></svg>Business for over 36 years</li>
  </ul>
  <ul class="contacts">
    <li><svg viewBox="0 0 10 10"><path d="M0 2h10v6H0z M0 2l5 3.5L10 2" /></svg>mark@brindlecrestmgmt.com</li>
    <li><svg viewBox="0 0 10 10"><circle cx="5" cy="5" r="4.5"/></svg>brindlecrestharborproperties.com</li>
    <li><svg viewBox="0 0 10 10"><path d="M5 0a3.6 3.6 0 0 1 3.6 3.6C8.6 6.2 5 10 5 10S1.4 6.2 1.4 3.6A3.6 3.6 0 0 1 5 0z"/></svg>18 Tessaly Court, Suite 4</li>
    <li class="no-icon">Palos Verdes Estates, CA 90318</li>
  </ul>
  <div class="stamp"></div>
  <div class="address-line" style="top:132px"></div>
  <div class="address-line" style="top:159px"></div>
  <div class="address-line" style="top:186px"></div>
</section>

</body>
</html>
```